The Corvane Agency

We are a pr, social media and strategy agency specializing in the pet industry. We would like a new dynamic design of our existing website. We think it is currently outdated and looks too corporate. We would like it to look more consumer oriented as we primarily market pet products. We would like warm imagery involving pets and while pets are fun, this is still a business website and needs to maintain a professional look. We are hired by business owners and executives.
I would like some of our work featured on the home page.
Our primary service tabs are:
Public Relations
Social Media
Product Consulting
Most of the content will remain the same but we are open to suggestions!
Our current website can be found at www.corvanepetpr.example.
We are open to other colors than in our logo and on our current page.
This is a design only project and will not require programming. The selected designer will need to provide at least one interior page in addition to the home page.

Industry/Entity Type

Pet

Requirements
Should not have
• Cartoon type figures. Pet puns.

```html
<!DOCTYPE html>
<html lang="en">
<head>
<meta charset="utf-8">
<title>The Corvane Agency</title>
<link href="https://fonts.googleapis.com/css2?family=Arimo:wght@400;700&family=Ubuntu:wght@400;500;700&display=swap" rel="stylesheet">
<style>
:root{
  --red:#ff1a24;
  --red-dark:#d80f18;
  --page:#ececec;
  --ink:#2b2b2b;
  --text:#444;
  --line:#d6d6d6;
  --white:#fff;
}
*{margin:0;padding:0;box-sizing:border-box}
html,body{width:1200px;height:1000px;overflow:hidden}
body{background:var(--page);font-family:Arimo,Arial,sans-serif;color:var(--text);position:relative}
.top-rule{position:absolute;left:0;top:0;width:1200px;height:5px;background:var(--red)}
.brand{position:absolute;left:90px;top:38px;width:170px;color:var(--red);font:400 22px/26px Ubuntu,sans-serif;display:flex;align-items:flex-start;gap:7px}
.brand-dot{width:7px;height:7px;border-radius:50%;background:var(--red);margin-top:10px;flex:none}
.divider{position:absolute;left:272px;top:25px;width:3px;height:92px;background:linear-gradient(#ececec,#cfcfcf,#ececec)}
.definition{position:absolute;left:305px;top:30px;width:235px;font-size:12px;line-height:20.5px;color:#555}
.definition b{font-weight:700;color:#333}
.social{position:absolute;left:871px;top:51px;display:flex;gap:8px}
.social span{width:32px;height:32px;border-radius:50%;background:var(--red)}
.nav{position:absolute;left:64px;top:133px;width:1070px;height:45px;background:linear-gradient(var(--red),var(--red-dark));border-radius:4px 4px 0 0;display:flex}
.nav a{color:var(--white);text-decoration:none;font:500 17px Ubuntu,sans-serif;display:flex;align-items:center;justify-content:center;border-right:1px solid #b80d14;height:100%}
.nav a:last-child{border-right:none}
.hero{position:absolute;left:65px;top:180px;width:1069px;height:450px;background:linear-gradient(160deg,#fff 0%,#f4f4f4 45%,#d8d8d8 100%);border-bottom:5px solid var(--red);overflow:hidden}
.hero-shape{position:absolute;left:0;top:0}
.hero-title{position:absolute;left:88px;top:48px;font:700 56px/67px Arimo,sans-serif;color:var(--ink);letter-spacing:-0.5px}
.hero-rule{position:absolute;left:89px;top:184px;width:511px;height:6px;background:var(--red)}
.hero-copy{position:absolute;left:89px;top:201px;font-size:24px;line-height:34px;color:#222;white-space:nowrap}
.hero-copy b{font-weight:400;color:#111}
.hero-photo{position:absolute;left:635px;top:40px;width:360px;height:340px;border-radius:45% 40% 20% 20%;background:radial-gradient(ellipse at 50% 40%,#e9d3aa,#d4b583 70%,rgba(212,181,131,0) 72%)}
.arrow{position:absolute;top:173px;width:36px;height:50px;background:#bdbdbd;display:flex;align-items:center;justify-content:center}
.arrow.prev{left:0}
.arrow.next{right:0}
.dots{position:absolute;left:92px;top:406px;display:flex;gap:11px}
.dots span{width:15px;height:15px;background:#d0d0d0}
.dots span.on{background:var(--red)}
.clients{position:absolute;left:65px;top:633px;width:1069px;height:102px;background:linear-gradient(#fff,#e6e6e6);display:flex;align-items:center}
.clients-label{width:165px;height:100%;border-right:1px solid var(--line);padding:26px 0 0 30px;font:700 23px/30px Ubuntu,sans-serif;color:#a9a9a9}
.client-list{display:flex;justify-content:space-around;flex:1}
.client{font:700 30px Arimo,sans-serif;color:#7b7b7b;display:flex;align-items:center;gap:8px}
.client i{width:12px;height:12px;background:#7b7b7b;display:block}
.content{position:absolute;left:65px;top:735px;width:1069px;height:265px;background:var(--white)}
.photo-frame{position:absolute;background:#d3d3d3;padding:7px}
.photo-fill{width:100%;height:100%}
.about-frame{left:28px;top:35px;width:306px;height:168px}
.about-frame .photo-fill{background:linear-gradient(100deg,#b8c6cc,#dfe3e2 45%,#6f6a6a 70%,#c4ccce)}
.team-frame{left:370px;top:33px;width:306px;height:168px}
.team-frame .photo-fill{background:linear-gradient(#f3ece6,#e0d6cc 55%,#3b3434 58%,#b89d86)}
.col-title{position:absolute;color:var(--red);font-size:17px;font-weight:400}
.col-text{position:absolute;font-size:14px;color:#444;white-space:nowrap}
.blog{position:absolute;left:720px;top:0;width:349px;height:265px;box-shadow:-6px 0 10px -6px rgba(0,0,0,.25);padding:36px 0 0 27px}
.blog h3{font-weight:400;font-size:17px;color:var(--red);padding:0 0 13px 7px;border-bottom:1px solid var(--line);width:293px}
.blog ul{list-style:none;width:295px}
.blog li{height:38px;border-bottom:1px solid var(--line);display:flex;align-items:center;font-size:14px;color:#444;gap:12px;padding-left:8px}
.blog li::before{content:"";width:5px;height:5px;background:var(--red)}
</style>
</head>
<body>
<div class="top-rule"></div>
<div class="brand"><span class="brand-dot"></span><span>The Corvane<br>Agency</span></div>
<div class="divider"></div>
<p class="definition"><b>Corvane</b> [kor-veyn] a (1): a driving force: (2): incentive, stimulus b: stimulus or encouragement resulting in increased activity.</p>
<div class="social"><span></span><span></span><span></span><span></span><span></span></div>

<nav class="nav">
  <a style="width:128px">Home</a>
  <a style="width:196px">Public Relations</a>
  <a style="width:172px">Social Media</a>
  <a style="width:222px">Product Consulting</a>
  <a style="width:170px">Case Studies</a>
  <a style="width:182px">Our Team</a>
</nav>

<section class="hero">
  <svg class="hero-shape" width="1069" height="450" aria-hidden="true"><polygon points="25,0 630,0 120,450 40,450" fill="#c8c8c8" opacity=".55"/><polygon points="630,0 1030,0 540,450 120,450" fill="#fff" opacity=".5"/></svg>
  <h1 class="hero-title">Redifining<br>Pet Products</h1>
  <div class="hero-rule"></div>
  <p class="hero-copy">The <b>Corvane Agency</b> knows what it takes to<br>successuflly market your Pet Product, whe-<br>ther it’s a new product or a rebrand and ex-<br>pand your target audience.</p>
  <div class="hero-photo" role="img" aria-label="Photo of a golden retriever lying down"></div>
  <div class="arrow prev"><svg width="14" height="20"><path d="M11 2 3 10l8 8" stroke="#fff" stroke-width="4" fill="none"/></svg></div>
  <div class="arrow next"><svg width="14" height="20"><path d="M3 2l8 8-8 8" stroke="#fff" stroke-width="4" fill="none"/></svg></div>
  <div class="dots"><span class="on"></span><span></span><span></span></div>
</section>

<section class="clients">
  <div class="clients-label">Featured<br>Clients</div>
  <div class="client-list">
    <span class="client">Verdel</span>
    <span class="client"><i></i>Norwick</span>
    <span class="client">Talvo</span>
    <span class="client">Norwick Canine</span>
  </div>
</section>

<section class="content">
  <div class="photo-frame about-frame"><div class="photo-fill" role="img" aria-label="Photo of a smiling businessman with colleagues behind him"></div></div>
  <h2 class="col-title" style="left:29px;top:221px">About Corvane</h2>
  <p class="col-text" style="left:29px;top:253px">PR has evolved from public relations to personal</p>
  <div class="photo-frame team-frame"><div class="photo-fill" role="img" aria-label="Group photo of the agency team standing in a row"></div></div>
  <h2 class="col-title" style="left:372px;top:218px">Our Team</h2>
  <p class="col-text" style="left:372px;top:251px">The driving force behind our success is the team</p>
  <aside class="blog">
    <h3>Most Recent Blog Post</h3>
    <ul>
      <li>Halvey Featured on Morning Brief</li>
      <li>The Power of Stress</li>
      <li>The Evolution of the Ideas: Brainstorming</li>
      <li>Can Giving Go Viral?</li>
      <li>Relationship Building</li>
    </ul>
  </aside>
</section>
</body>
</html>
```